Business Card for a recruitment agency specializing in engineers and geeks.

I am looking to create Business Card Design for my company.
That
## Company name:
Quorvant Inc.
Quorvant is a term coined from the following concepts.
1. geek + engineer
2. geek utopia
## Company Description:
The concept of the company is to be a recruitment agency that creates a paradise for geeky engineers. We want to be a place where engineers can have more freedom and ideal career support.
# Target.
The noun itself is often given to companies that want to hire engineers, geeks, and IT-related personnel, so it would be nice to get the impression that this company seems to have good engineers and IT personnel. There are many occasions where I meet with the human resources department, president, or senior management and give it to them.
# Atmosphere
We are happy with simplicity, but with an impact that will help people remember the company. The logo is based on a dinosaur that does programming, so it should be somewhat playful, but since it will basically be used in a business setting, please don't make it too silly.
# About the logo
See the attached files. The company logo represents our engineers smiling upward because of our work, with the motif of a dinosaur doing programming.
## Color
We will leave the color scheme to you, but since the logo is in black and white, colors with such a taste would fit well.
## file format
ai, psd, png, svg
Industry/Entity Type
human resource and employment agency
Contact Information for Business Card
Company name, address, email, tel, URL,logo
Colors
Designer to choose colors to be used in the design.

```html
<!DOCTYPE html>
<html lang="en">
<head>
<meta charset="utf-8">
<title>Quorvant Inc. — Business Card</title>
<link rel="stylesheet" href="https://fonts.googleapis.com/css2?family=Poppins:wght@300;400;500&display=swap">
<style>
  :root {
    --bg: #d9d9d9;
    --card: #1b1a1b;
    --edge: #e3101f;
    --accent: #e3101f;
    --text: #ffffff;
    --rule: #cfcfcf;
  }
  * { box-sizing: border-box; margin: 0; padding: 0; }
  html, body {
    width: 1200px;
    height: 800px;
    overflow: hidden;
    background: var(--bg);
    font-family: "Poppins", sans-serif;
  }
  .canvas {
    width: 1200px;
    height: 800px;
    display: flex;
    align-items: center;
    justify-content: center;
    gap: 60px;
  }
  .card {
    width: 525px;
    height: 300px;
    background: var(--card);
    border-bottom: 3px solid var(--edge);
    border-left: 2px solid var(--edge);
    position: relative;
    overflow: hidden;
  }

  /* Contact side */
  .card--contact {
    display: flex;
    align-items: center;
  }
  .identity {
    width: 235px;
    text-align: right;
    padding-right: 20px;
  }
  .identity__name {
    color: var(--accent);
    font-size: 24px;
    font-weight: 400;
    line-height: 1.1;
    letter-spacing: 0.2px;
  }
  .identity__title {
    color: var(--text);
    font-size: 15px;
    font-weight: 400;
    margin-top: 2px;
  }
  .divider {
    width: 1px;
    height: 110px;
    background: var(--rule);
  }
  .details {
    padding-left: 20px;
    color: var(--text);
    font-size: 12.5px;
    line-height: 1.5;
    font-weight: 400;
  }
  .details__address { margin-bottom: 6px; }
  .details__row {
    display: flex;
    align-items: center;
    gap: 9px;
  }
  .details__icon {
    width: 11px;
    height: 11px;
    flex: none;
  }

  /* Brand side */
  .card--brand {
    display: flex;
    align-items: center;
    justify-content: center;
  }
  .brand {
    display: flex;
    align-items: center;
    gap: 20px;
  }
  .brand__mark {
    width: 58px;
    height: 58px;
    border: 6px solid var(--text);
  }
  .brand__name {
    color: var(--text);
    font-size: 52px;
    font-weight: 400;
    letter-spacing: 1px;
  }
</style>
</head>
<body>
<main class="canvas">

  <section class="card card--contact" aria-label="Business card, contact side">
    <div class="identity">
      <p class="identity__name">Daniel Reyes</p>
      <p class="identity__title">President</p>
    </div>
    <div class="divider"></div>
    <div class="details">
      <p class="details__address">412 Birchwood Avenue<br>Fairview, Oregon 97024</p>
      <p class="details__row">
        <svg class="details__icon" viewBox="0 0 12 12" aria-hidden="true"><path d="M2.5 1 L4.5 1 L5.3 3.4 L4 4.4 Q5 6.9 7.6 8 L8.6 6.7 L11 7.5 L11 9.5 Q10 11 8.5 11 Q1 9.5 1 2.5 Q1 1.5 2.5 1 Z" fill="var(--accent)"/></svg>
        555-014-2738
      </p>
      <p class="details__row">
        <svg class="details__icon" viewBox="0 0 12 12" aria-hidden="true"><rect x="3" y="0.8" width="6" height="10.4" rx="1" fill="none" stroke="var(--accent)" stroke-width="1.4"/><circle cx="6" cy="9.3" r="0.7" fill="var(--accent)"/></svg>
        555-019-6481
      </p>
      <p class="details__row">
        <svg class="details__icon" viewBox="0 0 12 12" aria-hidden="true"><rect x="0.5" y="2" width="11" height="8" fill="var(--accent)"/><path d="M0.8 2.4 L6 6.6 L11.2 2.4" fill="none" stroke="var(--card)" stroke-width="1"/></svg>
        hello@quorvant.com
      </p>
      <p class="details__row">
        <svg class="details__icon" viewBox="0 0 12 12" aria-hidden="true"><circle cx="6" cy="6" r="5.5" fill="var(--accent)"/><path d="M0.5 6 H11.5 M6 0.5 Q2.8 6 6 11.5 M6 0.5 Q9.2 6 6 11.5" fill="none" stroke="var(--card)" stroke-width="0.8"/></svg>
        www.quorvant.com
      </p>
    </div>
  </section>

  <section class="card card--brand" aria-label="Business card, brand side">
    <div class="brand">
      <span class="brand__mark" aria-hidden="true"></span>
      <span class="brand__name">Quorvant</span>
    </div>
  </section>

</main>
</body>
</html>
```